Brane & Hollis LLC
Commercial Real Estate Invesment Group
Brane & Hollis LLC -
Creative Brief
www.braneandhollisllc.example
Fitz & Co.focuses on Undervalued Assets that are cash flowing and have great potential upside.And the elimination of risk.
left side
www.quellmorefunds.example/#/home
www.ridgewaysyndicate.example
www.vantor.example
I need a lot of help here I am of no use visually at all. I do not even know how to answer most of the questions to you
dawnp dawnp
Guys that was the most painful and hard decision I have had to make in a very very long time. Thank you all you are all great and all of your effort was and is greatly appreciated. You are all genuineness and I am a lucky to have had you participate in this.
brightforge brightforge
Hello PH, Please check you PM inbox. Thanks
pixelmonk pixelmonk
Hi PH, Please check your private message. thanks,
Hey to everybody. This going to be a hard selection to be a hard selection process, Everything is great and Thank you for all of you work. I need to talk to support and ask a few questions, that I asked some privately and did not get answers to. I have kept this open because one particular designer asked me to, And I have this other Restaurant thing going on, that has stalled my attention to this. I spent some time doing some time eliminating some just to get a clearer view. I will have pick a winner by Sunday, Thank you all so much
Can Somebody put any thought on the Trelby Hall project please. I am opening that in 3 weeks.
Qv I really like this #29 can you go back to Who we are? Keep the arrow and maybe look for another building for the pic on the right. Fernwright #28 is ok but please re-read the brief and the thread we are a Commercial Real Estate Co.. Can I see it with maybe retail pics, strip centers? Please. Thank you
Lumo 24 & 26 are great 25 a little residential in feel. The path everybody is on is fantastic. A little more about us as a business, we have been investing in Commercial Real Estate as a group for 10 years after moving from Residential we primarily focusing on retail strip centers. We focus of Cash Flow and Dividends return in 1-2 years. And return on Capital by year 5 or sooner. We have a track record of of high returns and not losing money.
LuNaPix7Kw3Fo LuNaPix7Kw3Fo
Hello@dawnp, This is my 1st design hope you like it please feel free to let me know the required changes so that your expectations are met. waiting for your feedback on design#19, #20 & #21 Regrds, LunaPix
Vobe the lay out again is good. The modern building is not working. Thanks
We are US based. Thank you
Vobe4web Vobe4web
Which location are you look at? In US or UK, please advise me further..
And Oh it should be Brane & Hollis LLC is that not on the Logo? And can we try the lettering in the header in black?
I like the layout and concept. But the pic's are residential we need to be looking more retail-City scapeish. Thanks
SiteAdmin SiteAdmin
Logo files have been attached. Kindly see Creative Brief Owen Hartley
pelnoart pelnoart
can u upload your LOGO ?

```html
<!DOCTYPE html>
<html lang="en">
<head>
<meta charset="utf-8">
<title>Brane &amp; Hollis LLC</title>
<link rel="stylesheet" href="https://fonts.googleapis.com/css2?family=Cinzel:wght@600&family=Arimo:wght@400;700&family=Tinos:wght@400;700&family=Archivo+Black&display=swap">
<style>
:root{
  --gold:#c8962f;
  --gold-light:#e2b65a;
  --gold-dark:#9c6f1c;
  --accent:#e0481d;
  --ink:#111;
  --text:#222;
  --white:#fff;
  --nav-panel:rgba(38,48,60,.62);
  --grey-bar-top:#d9d9d9;
  --grey-bar-bottom:#8d8d8d;
  --link:#d9481c;
}
*{box-sizing:border-box;margin:0;padding:0}
html,body{width:1200px;height:850px;overflow:hidden}
body{position:relative;background:linear-gradient(180deg,var(--gold-light) 0%,var(--gold) 45%,var(--gold-dark) 100%);font-family:'Arimo',Arial,sans-serif;color:var(--text)}
.brand{position:absolute;left:72px;top:28px;display:flex;align-items:center;gap:14px}
.brand-mark{width:40px;height:40px;background:var(--white)}
.brand-name{font-family:'Cinzel',serif;font-weight:600;font-size:32px;color:var(--white);line-height:1;white-space:nowrap}
.brand-tagline{position:absolute;left:126px;top:76px;font-size:11px;letter-spacing:1px;color:var(--white);text-transform:uppercase}
.contact-line{position:absolute;left:568px;top:68px;font-size:12.5px;font-weight:700;color:var(--accent);white-space:nowrap}
.quick-links{position:absolute;left:968px;top:40px;display:flex;gap:22px}
.quick-link{display:flex;flex-direction:column;align-items:center;gap:4px;font-size:11px;font-weight:700;color:var(--white)}
.quick-icon{width:48px;height:48px;background:var(--accent);border:2px solid #f6d6a0;display:flex;align-items:center;justify-content:center}
.page{position:absolute;left:28px;top:108px;width:1144px;height:662px;background:var(--white)}
.hero{position:absolute;left:0;top:0;width:1144px;height:407px;background:linear-gradient(180deg,#5e86b8 0%,#9fc0de 40%,#d7e6f1 70%,#8fa3b4 100%)}
.main-nav{position:absolute;left:68px;top:0;width:228px;height:407px;background:var(--nav-panel);padding-top:28px}
.main-nav a{display:flex;align-items:center;gap:10px;padding-left:16px;height:30px;color:var(--white);font-size:12px;font-weight:700;text-decoration:none;text-transform:uppercase}
.main-nav a::before{content:"";width:9px;height:9px;border:1px solid var(--white)}
.hero-copy{position:absolute;left:640px;top:226px;font-family:'Tinos',serif;font-weight:700;font-size:22px;line-height:30px;color:#2f3a48;white-space:nowrap}
.hero-button{position:absolute;left:960px;top:322px;width:142px;height:42px;background:#2a2f38;color:var(--white);font-family:'Tinos',serif;font-weight:700;font-size:21px;display:flex;align-items:center;justify-content:center}
.intro-bar{position:absolute;left:0;top:407px;width:1144px;height:63px;display:flex}
.intro-label{width:292px;display:flex;align-items:center;justify-content:center;font-size:30px;font-weight:700;color:var(--ink);border-bottom:2px solid #bbb}
.intro-welcome{flex:1;background:linear-gradient(180deg,var(--grey-bar-top),var(--grey-bar-bottom));display:flex;align-items:center;justify-content:center;font-family:'Archivo Black',sans-serif;font-size:30px;color:var(--white);letter-spacing:1px;-webkit-text-stroke:1px #777}
.photo{position:absolute}
.feature-text{position:absolute;font-size:12.5px;line-height:15px;color:var(--text)}
.feature-title{font-size:22px;font-weight:700;color:var(--ink);margin-bottom:6px}
.read-more{position:absolute;font-size:13px;color:var(--link)}
.site-footer{position:absolute;left:0;top:778px;width:1200px;text-align:center;color:var(--white);font-size:15px;line-height:26px}
.social{position:absolute;left:1006px;top:788px;display:flex;gap:10px}
.social span{width:42px;height:42px;background:#2f6fb0;border:2px solid var(--white)}
</style>
</head>
<body>
<header>
  <div class="brand"><span class="brand-mark"></span><span class="brand-name">Brane &amp; Hollis LLC</span></div>
  <div class="brand-tagline">Commercial Real Estate Investment Group</div>
  <div class="contact-line">Email: info@braneandhollisllc.example Tel: +1 800 555 0147</div>
  <div class="quick-links">
    <div class="quick-link"><span class="quick-icon"><svg width="28" height="28" viewBox="0 0 28 28"><path d="M4 14 L14 5 L24 14 M7 12 V23 H12 V17 H16 V23 H21 V12" fill="none" stroke="#fff" stroke-width="2.5"/></svg></span>HOME</div>
    <div class="quick-link"><span class="quick-icon"><svg width="28" height="28" viewBox="0 0 28 28"><rect x="4" y="7" width="20" height="14" fill="none" stroke="#fff" stroke-width="2.5"/><path d="M4 7 L14 15 L24 7" fill="none" stroke="#fff" stroke-width="2.5"/></svg></span>CONTACT US</div>
  </div>
</header>
<main class="page">
  <section class="hero" role="img" aria-label="City skyline under a bright blue sky with a glowing globe">
    <nav class="main-nav">
      <a>Home</a><a>Our Approach</a><a>Who We Are</a><a>What We Invest In</a><a>Contact Us</a>
    </nav>
    <p class="hero-copy">We are in&nbsp; the heart of the world<br>Before you think, we have your location<br>With full of peace and happiness&nbsp; comfort</p>
    <div class="hero-button">Read more</div>
  </section>
  <div class="intro-bar">
    <div class="intro-label">Our Company</div>
    <div class="intro-welcome">Welcome to BRANE &amp; HOLLIS LLC</div>
  </div>
  <div class="photo" role="img" aria-label="Business handshake with a card" style="left:0;top:477px;width:292px;height:110px;background:linear-gradient(135deg,#e8e8e8,#8a8a8a 60%,#2a2a2a)"></div>
  <p class="feature-text" style="left:0;top:592px;width:292px">Brane &amp; Hollis focuses on Undervalued Assets that are cash flowing and have great potential upside.And the elimination of risk.</p>
  <span class="read-more" style="left:210px;top:640px">read more</span>
  <div class="photo" role="img" aria-label="Modern glass office tower" style="left:312px;top:477px;width:106px;height:170px;background:linear-gradient(180deg,#9cb6cc,#5a7288 60%,#3a4a58)"></div>
  <div class="feature-text" style="left:428px;top:477px;width:282px">
    <div class="feature-title">Property 1</div>
    Brane &amp; Hollis focuses on Undervalued Assets that are cash flowing and have great potential upside.And the elimination of risk.&nbsp; Brane &amp; Hollis focuses on Undervalued Assets that are cash flowing and have great potential upside.And the elimination of risk. Brane &amp; Hollis focuses on Undervalued Assets
  </div>
  <span class="read-more" style="left:648px;top:640px">read more</span>
  <div class="photo" role="img" aria-label="Curved high-rise buildings against the sky" style="left:737px;top:477px;width:110px;height:170px;background:linear-gradient(180deg,#b9c9d8,#7d8fa0 55%,#4c5864)"></div>
  <div class="feature-text" style="left:860px;top:477px;width:284px">
    <div class="feature-title">Property 1</div>
    Brane &amp; Hollis focuses on Undervalued Assets that are cash flowing and have great potential upside.And the elimination of risk.&nbsp; Brane &amp; Hollis focuses on Undervalued Assets that are cash flowing and have great potential upside.And the elimination of risk. Brane &amp; Hollis focuses on Undervalued Assets
  </div>
  <span class="read-more" style="left:1080px;top:640px">read more</span>
</main>
<footer class="site-footer">
  <div>Home | Our Approach | Who we are | What we Invest in | Contact Us</div>
  <div>Copyright@2011 Brane &amp; Hollis LLC</div>
</footer>
<div class="social"><span></span><span></span><span></span></div>
</body>
</html>
```